7 P's for Healthcare Companies - Textbook Graphic

Can you create a graphic for me for a medical textbook? The goal is to show 7 critical features of a healthcare startup and the audience is physicians with limited business backgrounds.

Please include a picture of young, male emergency physician in the middle of the graphic. Show them evaluating an idea. Can you surround the physician with bold writing for the seven components, and use brief descriptions and simple images or graphics to illustrate the point?

The image should be somewhat formal, but it's OK to be lighthearded.

The seven P's and brief descriptions include the following:
Product: what is their market solution?
(Intellectual) Property: do they have a patent or trademark?
Product Clearance: how will they get QRB approval and TPW clearance?
Payment: how will they make money?
Pilots: have they applied their product in a healthcare setting?
Physician and Patient feedback: Do doctors and patients like their product?
Publication: do they have evidence their product works?

More detail and information is available at this website: https://brenvolt.com/blog/uncategorized/healthcare-framework/

I will need to own this image

```html
<!DOCTYPE html>
<html lang="en">
<head>
<meta charset="utf-8">
<title>7 P's for Healthcare Companies</title>
<link rel="stylesheet" href="https://fonts.googleapis.com/css2?family=Oswald:wght@700&family=Roboto+Condensed:wght@300&display=swap">
<style>
  :root {
    --page-bg: #58595b;
    --card-bg: #f3f3f4;
    --frame-green: #a6ce39;
    --title-grey: #58585a;
    --text-grey: #58585a;
    --ring-blue: #0ea5dd;
    --green-light: #d2dc2a;
    --green-mid: #9ccc3c;
    --green-dark: #4aa82c;
    --green-icon: #3f9f1e;
    --blue-light: #1fcbf2;
    --blue-mid: #0a9be3;
    --blue-dark: #0a6fcf;
    --blue-icon: #0b44c9;
  }
  * { box-sizing: border-box; margin: 0; padding: 0; }
  html, body { width: 1200px; height: 1200px; overflow: hidden; }
  body { background: var(--page-bg); position: relative; font-family: "Roboto Condensed", "Arial Narrow", sans-serif; }

  .card {
    position: absolute; left: 110px; top: 110px; width: 979px; height: 979px;
    border-radius: 38px;
    background: linear-gradient(180deg, #fbfbfb 0%, #ececed 100%);
    box-shadow: 14px 16px 30px rgba(0,0,0,0.35);
    overflow: hidden;
  }
  .card-frame {
    position: absolute; left: 30px; top: 30px; width: 919px; height: 919px;
    border: 2px solid var(--frame-green); border-radius: 20px;
  }

  .hex { position: absolute; width: 130px; height: 143px; }

  .label { position: absolute; color: var(--text-grey); }
  .label h2 {
    font-family: "Oswald", "Arial Narrow", sans-serif; font-weight: 700;
    font-size: 33px; line-height: 33px; letter-spacing: -0.3px;
    color: var(--title-grey); text-transform: uppercase;
    transform: scaleX(0.86); transform-origin: center;
  }
  .label p { font-weight: 300; font-size: 20px; line-height: 22px; margin-top: 6px; }
  .label.center { text-align: center; transform: translateX(-50%); white-space: nowrap; }
  .label.right { text-align: right; white-space: nowrap; }
  .label.right h2 { transform-origin: right; }
  .label.left { text-align: left; white-space: nowrap; }
  .label.left h2 { transform-origin: left; }

  .hub { position: absolute; left: 0; top: 0; width: 979px; height: 979px; pointer-events: none; }
  .physician {
    position: absolute; left: 325px; top: 368px; width: 330px; height: 611px;
  }
</style>
</head>
<body>
<div class="card">
  <div class="card-frame"></div>

  <svg class="hub" viewBox="0 0 979 979" aria-hidden="true">
    <defs>
      <linearGradient id="hub-fill" x1="0" y1="0" x2="1" y2="0">
        <stop offset="0" stop-color="#0aa6e0"/>
        <stop offset="0.5" stop-color="#3bb8a8"/>
        <stop offset="1" stop-color="#a3cf3c"/>
      </linearGradient>
      <linearGradient id="hex-green" x1="0" y1="0" x2="1" y2="1">
        <stop offset="0" stop-color="var(--green-light)"/>
        <stop offset="0.55" stop-color="var(--green-mid)"/>
        <stop offset="1" stop-color="var(--green-dark)"/>
      </linearGradient>
      <linearGradient id="hex-blue" x1="0" y1="0" x2="1" y2="1">
        <stop offset="0" stop-color="var(--blue-light)"/>
        <stop offset="0.5" stop-color="var(--blue-mid)"/>
        <stop offset="1" stop-color="var(--blue-dark)"/>
      </linearGradient>
      <linearGradient id="coat" x1="0" y1="0" x2="0" y2="1">
        <stop offset="0" stop-color="#e9e4df"/>
        <stop offset="0.5" stop-color="#f4f4f5"/>
        <stop offset="1" stop-color="#dcdde0"/>
      </linearGradient>
    </defs>
    <circle cx="490" cy="526" r="168" fill="url(#hub-fill)"/>
    <circle cx="490" cy="526" r="193" fill="none" stroke="var(--ring-blue)" stroke-width="4"/>
    <g fill="var(--ring-blue)">
      <circle cx="490" cy="335" r="12"/>
      <circle cx="360" cy="384" r="12"/>
      <circle cx="619" cy="384" r="12"/>
      <circle cx="304" cy="483" r="12"/>
      <circle cx="677" cy="483" r="12"/>
      <circle cx="314" cy="601" r="12"/>
      <circle cx="666" cy="601" r="12"/>
    </g>
  </svg>

  <svg class="physician" viewBox="0 0 330 611" role="img" aria-label="Illustration of a young male emergency physician in a white coat with a stethoscope, hand on chin, evaluating an idea">
    <path d="M120 0 H210 Q250 0 250 60 V250 Q330 270 330 340 V611 H0 V340 Q0 270 80 250 V60 Q80 0 120 0 Z" fill="url(#coat)"/>
  </svg>

  <!-- Product -->
  <svg class="hex" style="left:418px;top:69px" viewBox="0 0 130 143" aria-hidden="true">
    <path d="M65 5 L124 39 V104 L65 138 L6 104 V39 Z" fill="url(#hex-blue)" stroke="url(#hex-blue)" stroke-width="10" stroke-linejoin="round"/>
    <path d="M65 20 L111 47 V96 L65 123 L19 96 V47 Z" fill="none" stroke="rgba(255,255,255,0.45)" stroke-width="1.2" stroke-linejoin="round"/>
    <g fill="var(--blue-icon)">
      <rect x="60" y="38" width="10" height="26"/>
      <rect x="52" y="46" width="26" height="10"/>
      <rect x="44" y="92" width="16" height="4"/>
      <rect x="70" y="92" width="16" height="4"/>
    </g>
    <g fill="none" stroke="var(--blue-icon)" stroke-width="6" stroke-linecap="round">
      <path d="M40 62 Q36 80 58 86"/>
      <path d="M90 62 Q94 80 72 86"/>
    </g>
  </svg>
  <div class="label center" style="left:490px;top:230px">
    <h2>Product</h2>
    <p>What is their market solution?</p>
  </div>

  <!-- Property -->
  <svg class="hex" style="left:154px;top:109px" viewBox="0 0 130 143" aria-hidden="true">
    <path d="M65 5 L124 39 V104 L65 138 L6 104 V39 Z" fill="url(#hex-green)" stroke="url(#hex-green)" stroke-width="10" stroke-linejoin="round"/>
    <path d="M65 20 L111 47 V96 L65 123 L19 96 V47 Z" fill="none" stroke="rgba(255,255,255,0.45)" stroke-width="1.2" stroke-linejoin="round"/>
    <g fill="var(--green-icon)">
      <rect x="48" y="40" width="34" height="54"/>
      <rect x="34" y="56" width="12" height="38"/>
      <rect x="84" y="56" width="12" height="38"/>
    </g>
    <g fill="var(--green-light)">
      <circle cx="65" cy="52" r="7"/>
      <rect x="52" y="66" width="6" height="5"/><rect x="62" y="66" width="6" height="5"/><rect x="72" y="66" width="6" height="5"/>
      <rect x="52" y="76" width="6" height="5"/><rect x="62" y="76" width="6" height="5"/><rect x="72" y="76" width="6" height="5"/>
      <rect x="37" y="62" width="6" height="4"/><rect x="37" y="72" width="6" height="4"/>
      <rect x="87" y="62" width="6" height="4"/><rect x="87" y="72" width="6" height="4"/>
    </g>
    <g fill="var(--green-icon)"><rect x="63" y="48" width="4" height="8"/><rect x="61" y="50" width="8" height="4"/></g>
  </svg>
  <div class="label center" style="left:219px;top:270px">
    <h2>Property</h2>
    <p>Do they have a patent<br>or trademark?</p>
  </div>

  <!-- Payment -->
  <svg class="hex" style="left:677px;top:109px" viewBox="0 0 130 143" aria-hidden="true">
    <path d="M65 5 L124 39 V104 L65 138 L6 104 V39 Z" fill="url(#hex-green)" stroke="url(#hex-green)" stroke-width="10" stroke-linejoin="round"/>
    <path d="M65 20 L111 47 V96 L65 123 L19 96 V47 Z" fill="none" stroke="rgba(255,255,255,0.45)" stroke-width="1.2" stroke-linejoin="round"/>
    <circle cx="72" cy="54" r="14" fill="none" stroke="var(--green-icon)" stroke-width="4"/>
    <text x="72" y="61" text-anchor="middle" font-family="Oswald, sans-serif" font-weight="700" font-size="18" fill="var(--green-icon)">$</text>
    <path d="M40 82 Q60 72 76 80 L98 74 Q104 76 98 82 L74 94 Q60 96 46 92 Z" fill="var(--green-icon)"/>
    <rect x="30" y="80" width="10" height="16" rx="2" transform="rotate(-25 35 88)" fill="var(--green-icon)"/>
  </svg>
  <div class="label center" style="left:742px;top:270px">
    <h2>Payment</h2>
    <p>How will they<br>make money?</p>
  </div>

  <!-- Publication -->
  <svg class="hex" style="left:86px;top:368px" viewBox="0 0 130 143" aria-hidden="true">
    <path d="M65 5 L124 39 V104 L65 138 L6 104 V39 Z" fill="url(#hex-blue)" stroke="url(#hex-blue)" stroke-width="10" stroke-linejoin="round"/>
    <path d="M65 20 L111 47 V96 L65 123 L19 96 V47 Z" fill="none" stroke="rgba(255,255,255,0.45)" stroke-width="1.2" stroke-linejoin="round"/>
    <rect x="38" y="52" width="46" height="32" rx="2" fill="none" stroke="var(--blue-icon)" stroke-width="4"/>
    <path d="M30 88 H92 L88 94 H34 Z" fill="var(--blue-icon)"/>
    <circle cx="84" cy="50" r="12" fill="var(--blue-icon)"/>
    <path d="M74 56 L70 66 L80 60 Z" fill="var(--blue-icon)"/>
    <g fill="var(--blue-light)"><rect x="82.5" y="43" width="3" height="14"/><rect x="77" y="48.5" width="14" height="3"/></g>
  </svg>
  <div class="label center" style="left:151px;top:528px">
    <h2>Publication</h2>
    <p>Do they have evidence<br>their product works?</p>
  </div>

  <!-- Pilots -->
  <svg class="hex" style="left:757px;top:368px" viewBox="0 0 130 143" aria-hidden="true">
    <path d="M65 5 L124 39 V104 L65 138 L6 104 V39 Z" fill="url(#hex-blue)" stroke="url(#hex-blue)" stroke-width="10" stroke-linejoin="round"/>
    <path d="M65 20 L111 47 V96 L65 123 L19 96 V47 Z" fill="none" stroke="rgba(255,255,255,0.45)" stroke-width="1.2" stroke-linejoin="round"/>
    <rect x="36" y="44" width="54" height="46" rx="3" fill="var(--blue-icon)"/>
    <g fill="var(--blue-mid)">
      <circle cx="46" cy="60" r="3"/><circle cx="56" cy="60" r="3"/><circle cx="66" cy="60" r="3"/>
      <circle cx="46" cy="70" r="3"/><circle cx="56" cy="70" r="3"/>
      <circle cx="46" cy="80" r="3"/><circle cx="56" cy="80" r="3"/>
    </g>
    <circle cx="84" cy="84" r="15" fill="var(--blue-icon)" stroke="var(--blue-mid)" stroke-width="3"/>
    <path d="M84 75 V85 H92" fill="none" stroke="var(--blue-light)" stroke-width="3"/>
  </svg>
  <div class="label center" style="left:822px;top:528px">
    <h2>Pilots</h2>
    <p>Have they applied<br>their product in a<br>healthcare setting?</p>
  </div>

  <!-- Product Clearance -->
  <svg class="hex" style="left:154px;top:643px" viewBox="0 0 130 143" aria-hidden="true">
    <path d="M65 5 L124 39 V104 L65 138 L6 104 V39 Z" fill="url(#hex-green)" stroke="url(#hex-green)" stroke-width="10" stroke-linejoin="round"/>
    <path d="M65 20 L111 47 V96 L65 123 L19 96 V47 Z" fill="none" stroke="rgba(255,255,255,0.45)" stroke-width="1.2" stroke-linejoin="round"/>
    <rect x="42" y="44" width="40" height="52" rx="3" fill="var(--green-icon)"/>
    <rect x="54" y="38" width="16" height="10" rx="3" fill="var(--green-icon)"/>
    <g fill="var(--green-light)"><rect x="49" y="58" width="26" height="4"/><rect x="49" y="67" width="20" height="4"/><rect x="49" y="76" width="14" height="4"/></g>
    <path d="M86 72 L92 78 L70 100 L62 102 L64 94 Z" fill="var(--green-icon)" stroke="var(--green-mid)" stroke-width="2"/>
  </svg>
  <div class="label right" style="right:695px;top:803px">
    <h2>Product<br>Clearance</h2>
    <p>How will they get QRB approval<br>and TPW clearance?</p>
  </div>

  <!-- Physician and Patient Feedback -->
  <svg class="hex" style="left:688px;top:643px" viewBox="0 0 130 143" aria-hidden="true">
    <path d="M65 5 L124 39 V104 L65 138 L6 104 V39 Z" fill="url(#hex-green)" stroke="url(#hex-green)" stroke-width="10" stroke-linejoin="round"/>
    <path d="M65 20 L111 47 V96 L65 123 L19 96 V47 Z" fill="none" stroke="rgba(255,255,255,0.45)" stroke-width="1.2" stroke-linejoin="round"/>
    <g fill="var(--green-icon)">
      <circle cx="42" cy="56" r="7"/><path d="M30 84 Q30 66 42 66 Q54 66 54 84 Z"/>
      <circle cx="88" cy="56" r="7"/><path d="M76 84 Q76 66 88 66 Q100 66 100 84 Z"/>
      <circle cx="65" cy="50" r="9"/><path d="M50 86 Q50 62 65 62 Q80 62 80 86 Z"/>
      <circle cx="65" cy="88" r="13" stroke="var(--green-mid)" stroke-width="3"/>
    </g>
    <g fill="var(--green-light)"><rect x="63" y="81" width="4" height="14"/><rect x="58" y="86" width="14" height="4"/></g>
  </svg>
  <div class="label left" style="left:690px;top:803px">
    <h2>Physician and<br>Patient Feedback</h2>
    <p>Do doctors and patients<br>like their product?</p>
  </div>
</div>
</body>
</html>
```